Flyer promoting Velmora's workshops and credentials

We run Training workshops for the data analyst community. We'd like a flyer to sell our services using a style and colour scheme consistent with our website www.velmoraskills.co.uk . I've attached some background info and some existing e-brochures for different workshops to give a flavour for content (but these are poorly designed and we don't want a similar design!!). There's also an overview document which gives more direction. The flyer will be sent with an accompanying letter to Learning & Development decision makers as well as Anlaytical team managers. It's purpose would be to generate enquiries and bookings for primarliy our flagship workshop 'Turning Figures Into Real Results'.

Target Market(s)

Learning and Development senior managers
Analytical team managers

Industry/Entity Type

Training

Font styles to use
Other font styles liked:
• Similar to website for consistency

Requirements
Must have
• Good copy! Slick design more in line with European (UK) style advertising rather than US.
Nice to have
• Some humour,
Should not have
• should not be as boring and non-sales based as the website!! Website is not a great example!

```html
<!DOCTYPE html>
<html lang="en">
<head>
<meta charset="utf-8">
<title>Velmora – Workshops for Data Analysts</title>
<link href="https://fonts.googleapis.com/css2?family=Lora:ital,wght@1,400;1,700&family=Open+Sans:wght@400;600&display=swap" rel="stylesheet">
<style>
  :root {
    --navy: #1c3a6e;
    --navy-deep: #0d2457;
    --blue-bright: #1f5fb8;
    --orange: #f08a1c;
    --gold: #f6b23a;
    --ink: #111111;
    --white: #ffffff;
  }
  * { margin: 0; padding: 0; box-sizing: border-box; }
  html, body { width: 848px; height: 1200px; overflow: hidden; }
  body {
    position: relative;
    background: radial-gradient(ellipse at 70% 45%, var(--blue-bright) 0%, #143f8f 45%, var(--navy-deep) 100%);
    font-family: 'Lora', Georgia, serif;
    font-style: italic;
    color: var(--ink);
  }
  .band-back {
    position: absolute; left: 0; top: 46px; width: 848px; height: 50px;
    background: var(--navy-deep);
  }
  .page {
    position: absolute; left: 0; top: 0; width: 848px; height: 1200px;
    background: var(--white);
    clip-path: polygon(36px 0, 758px 0, 812px 1200px, 90px 1200px);
  }
  .header-band {
    position: absolute; left: 230px; top: 46px; width: 618px; height: 50px;
    background: var(--navy);
  }
  .headline {
    position: absolute; left: 242px; top: 47px; width: 500px;
    color: var(--gold); font-size: 19px; line-height: 24px; font-style: italic; font-weight: 400;
  }
  .brand {
    position: absolute; left: 42px; top: 24px;
    font-weight: 700; font-style: italic;
    font-size: 46px; color: var(--navy); line-height: 1;
  }
  .tagline {
    position: absolute; left: 48px; top: 101px;
    color: var(--orange); font-size: 12.5px; font-style: italic;
  }
  .mascot {
    position: absolute; left: 752px; top: 12px; width: 72px; height: 100px;
    background: linear-gradient(180deg, #f39a2a 0%, #d7d7d7 100%);
    border-radius: 10px;
  }
  .photo { position: absolute; }
  .photo-team { left: 62px; top: 130px; width: 695px; height: 170px;
    background: linear-gradient(90deg, #c9ccd2 0%, #eef0f3 45%, #cfd6e0 100%); }
  .photo-class { left: 68px; top: 476px; width: 708px; height: 170px;
    background: linear-gradient(90deg, #6d5a4a 0%, #e6e6e6 40%, #f2f2f2 60%, #8a8d94 100%); }
  .copy {
    position: absolute; font-size: 16px; line-height: 20.6px; text-align: justify;
    font-style: italic; font-weight: 400;
  }
  .intro { left: 62px; top: 320px; width: 702px; }
  .clients { left: 76px; top: 656px; width: 702px; }
  .brand-inline { color: var(--orange); font-weight: 700; }
  .section-title {
    position: absolute; right: 74px; top: 799px;
    color: var(--orange); font-weight: 700; font-style: italic; font-size: 16px;
  }
  .rule { position: absolute; left: 122px; top: 821px; width: 652px; height: 1px; background: #222; }
  .lead { left: 78px; top: 830px; width: 698px; }
  .list { position: absolute; list-style: none; font-size: 16px; line-height: 20.6px; font-style: italic; }
  .list-main { left: 110px; top: 890px; }
  .list-main li { padding-left: 20px; position: relative; }
  .list-main li::before {
    content: ""; position: absolute; left: 0; top: 6px; width: 9px; height: 9px; background: var(--navy);
  }
  .list-sub { left: 160px; top: 972px; }
  .list-sub li { padding-left: 20px; position: relative; }
  .list-sub li::before {
    content: ""; position: absolute; left: 0; top: 5px; width: 10px; height: 10px; border-radius: 50%; background: var(--navy);
  }
  .flagship { color: var(--orange); font-weight: 700; }
  .footer-band {
    position: absolute; left: 0; top: 1138px; width: 848px; height: 44px;
    background: var(--navy-deep);
    font-family: 'Open Sans', Arial, sans-serif; font-style: normal;
    color: var(--white); text-align: center; font-size: 12px; line-height: 18px;
    padding: 4px 0 0 80px;
  }
  .footer-band strong { font-weight: 600; }
</style>
</head>
<body>
  <div class="band-back"></div>
  <div class="page"></div>
  <div class="header-band"></div>
  <div class="brand">Velmora</div>
  <div class="tagline">Workshops for Data Analysts</div>
  <p class="headline">Do you want your data analysts to have a greater impact on your organisation &amp; be more productive?</p>
  <div class="mascot" role="img" aria-label="Illustration of an orange figure relaxing in an armchair with a tablet"></div>

  <div class="photo photo-team" role="img" aria-label="Photo of smiling business professionals with a tablet showing charts"></div>

  <p class="copy intro"><span class="brand-inline">Velmora</span> understand that technical ability alone is not enough to be effective as a data analyst. Whether you’re an insight expert, a risk analyst or a Business Intelligence professional, the best analysts employ a range of complimentary soft skills in order to be able to effectively plan, present and communicate ideas, results and reports. Our range of workshops aim to help analysts become more commercially focussed and employ some key techniques and behaviours in order to maximise their influence over their key decision makers.</p>

  <div class="photo photo-class" role="img" aria-label="Photo of a presenter at a whiteboard addressing a workshop audience"></div>

  <p class="copy clients">Our workshops have been attended by many of the UK’s largest organisations and many international organisations too including Larkfield, Norbridge Bank, Greywater Energy and XXX. Our workshops are run by experienced professionals including Daniel Ashcombe, Velmora’s founder and the facilitator for Velmora’s flagship workshop ‘Turning Figures Into Real Results’ - a workshop that has been running for over 10 years and become an essential ‘cornerstone’ development session for many of our regular clients’ analysts.</p>

  <h2 class="section-title">Key Highlight of workshops</h2>
  <div class="rule"></div>

  <p class="copy lead">Essential development workshops for data analysts focus on how to interact with their customers and present themselves and their work. Key highlights of the workshops are:</p>

  <ul class="list list-main">
    <li>Workshops developed by highly experienced practitioners</li>
    <li>Small audiences to keep interaction high and maximise learning experience.</li>
    <li>‘<span class="flagship">Turning Figures Into Real Results</span>’ (flagship workshop) main selling points</li>
  </ul>

  <ul class="list list-sub">
    <li>CPD accredited</li>
    <li>Unique</li>
    <li>99.4% of past attendees would recommend the workshop to other analysts</li>
    <li>Has plenty of positive testimonials</li>
    <li>Been attended by UK’s largest organisations (and regularly by some).</li>
    <li>Been running for over 10 years</li>
    <li>Cornerstone workshop in the development of analysts</li>
  </ul>

  <footer class="footer-band">
    <strong>www.velmoraskills.co.uk | info@velmoraskills.co.uk</strong><br>
    #4 Alder Court, Hazelford, Stockport, Cheshire, SK9 4QT | Tel: 0161 555 0142 | Fax: 0845 5550187
  </footer>
</body>
</html>
```